Need a PowerPoint that reflects the company brand has great graphics.

Want a PowerPoint for a financial advisory firm that has continuity. Our practice builds financial advisory plans for individuals. We have three sub divisions so I need some slides branded to reflect each. To better understand these requirements please visit our website at: http://lindenpr.kzqt4-rv7.b9servo.com

I want the colors of the logo to be the focal point throughout the slide designs. This needs to look extremely professional.

```html
<!DOCTYPE html>
<html lang="en">
<head>
<meta charset="utf-8">
<title>Linden Peak Management – Presentation Slides</title>
<link href="https://fonts.googleapis.com/css2?family=Oswald:wght@700&family=Open+Sans:wght@400;600;700&display=swap" rel="stylesheet">
<style>
:root{
  --blue:#1b5cb5;
  --blue-deep:#154a96;
  --orange:#f7a01d;
  --ink:#2b2b2b;
  --muted:#6b6b6b;
  --stage-light:#f0f0f0;
  --stage-dark:#3a3a3a;
  --white:#ffffff;
}
*{margin:0;padding:0;box-sizing:border-box}
html,body{width:1200px;height:2250px;overflow:hidden}
body{position:relative;background:var(--stage-light);font-family:"Open Sans",Arial,sans-serif;color:var(--ink)}

.stage-hero{position:absolute;left:0;top:0;width:1200px;height:805px;background:linear-gradient(180deg,#f7f7f7,#e9e9e9)}
.stage-grid{position:absolute;left:0;top:805px;width:1200px;height:1445px;background:var(--stage-dark)}

.hero-frame{position:absolute;left:216px;top:190px;width:769px;height:433px;box-shadow:0 18px 40px rgba(0,0,0,.18)}
.hero-frame .slide{transform:scale(1.4);transform-origin:0 0;left:0;top:0}

.slide{position:absolute;width:549px;height:309px;background:var(--white);overflow:hidden;box-shadow:0 6px 18px rgba(0,0,0,.35)}
.slide::before,.slide::after{content:"";position:absolute;bottom:0;width:40px;height:38px;background:var(--blue)}
.slide::before{left:0;clip-path:polygon(0 0,100% 100%,0 100%)}
.slide::after{right:0;clip-path:polygon(100% 0,100% 100%,0 100%)}
.slide svg.art{position:absolute;left:0;top:0;width:549px;height:309px}

.slide-footer{position:absolute;left:0;right:0;bottom:11px;text-align:center;font-size:7.5px;letter-spacing:1.6px;color:#555}
.page-no{position:absolute;right:44px;bottom:10px;font-size:7px;color:var(--blue)}

.slide-title{position:absolute;left:16px;top:14px;font-size:11px;font-weight:700;color:var(--blue);padding-bottom:3px;border-bottom:1.5px solid var(--orange)}
.slide-title .accent{color:var(--orange)}

.mini-brand{position:absolute;right:16px;top:12px;text-align:center;color:var(--blue);font-weight:700;line-height:1}
.mini-brand .name{font-size:9.5px}
.mini-brand .sub{font-size:5px;letter-spacing:1.2px;margin-top:2px}

.copy{font-size:6px;line-height:1.55;color:#333}
.copy-center{text-align:center}
.copy-strong{font-weight:700}

/* cover */
.cover-brand{position:absolute;right:22px;top:14px;width:150px;text-align:center;color:var(--blue);font-weight:700;line-height:1}
.cover-brand .mark{display:block;width:24px;height:24px;margin:0 auto 5px;background:var(--orange)}
.cover-brand .name{font-size:17px}
.cover-brand .sub{font-size:8px;letter-spacing:2.4px;margin-top:3px}
.cover-headline{position:absolute;left:306px;top:126px;width:236px;text-align:center;font-family:"Oswald",Impact,sans-serif;font-weight:700;line-height:1.02}
.cover-headline .l1{display:block;font-size:26px;color:var(--orange)}
.cover-headline .l2{display:block;font-size:26px;color:var(--blue)}
.cover-headline .l3{display:block;font-size:46px;color:var(--orange);line-height:1.05}
.cover-url{position:absolute;left:182px;bottom:12px;font-size:7.5px;letter-spacing:1.6px;color:#555}
.cover-rule{position:absolute;left:392px;bottom:16px;width:124px;height:1px;background:var(--blue)}

/* service icons slide */
.service-caption{position:absolute;top:214px;width:120px}

/* bullets slide */
.list-heading{position:absolute;left:284px;top:64px;font-size:9.5px;font-weight:700;color:var(--blue);padding-bottom:2px;border-bottom:1.2px solid var(--orange)}
.list-heading .accent{color:var(--orange)}
.point{position:absolute;left:284px;width:250px;padding-left:14px}
.point::before{content:"";position:absolute;left:0;top:1px;width:6px;height:6px;border:1.5px solid var(--orange);border-radius:50%}

.band-copy{position:absolute;left:16px;top:82px;width:232px;color:var(--white)}
.band-copy p+p{margin-top:8px}

.tab-text{position:absolute;top:55px;width:90px;text-align:center;font-size:5.5px;color:var(--white);line-height:22px}

.profile-copy{position:absolute;width:110px}
.profile-copy .label{font-size:6px;font-weight:700;margin-bottom:2px}
.col-heading{font-size:6px;font-weight:700;margin-bottom:3px}

/* contact slide */
.contact-brand{position:absolute;left:0;right:0;top:20px;text-align:center;color:var(--blue);font-weight:700;line-height:1}
.contact-brand .name{font-size:20px}
.contact-brand .sub{font-size:9px;letter-spacing:2.6px;margin-top:4px}
.contact-band{position:absolute;left:0;right:0;top:82px;height:94px;background:var(--orange);color:var(--white);text-align:center;padding:10px 26px 0}
.contact-band h3{font-size:11px;font-weight:600;margin-bottom:5px}
.contact-band p{font-size:6px;line-height:1.6}
.call-line{position:absolute;left:0;right:0;top:196px;text-align:center;font-size:11.5px;font-weight:700;color:var(--orange)}
.call-line .phone{color:var(--ink);margin-left:6px}
.info-line{position:absolute;left:0;right:0;text-align:center;font-size:5.5px;color:#333}
.info-line .dot{display:inline-block;width:4px;height:4px;border-radius:50%;background:var(--blue);margin-right:4px;vertical-align:middle}
</style>
</head>
<body>

<div class="stage-hero"></div>
<div class="stage-grid"></div>

<!-- large cover -->
<div class="hero-frame">
  <section class="slide cover">
    <svg class="art" viewBox="0 0 549 309" aria-hidden="false">
      <defs>
        <linearGradient id="deskA" x1="0" y1="0" x2="1" y2="1">
          <stop offset="0" stop-color="#2f3a4b"/><stop offset=".55" stop-color="#8d939c"/><stop offset="1" stop-color="#d9dbde"/>
        </linearGradient>
      </defs>
      <polygon points="0,0 410,0 138,309 0,309" fill="var(--blue)"/>
      <g role="img" aria-label="Photo of business advisors reviewing documents at a desk">
        <polygon points="0,0 272,0 70,210 0,180" fill="url(#deskA)"/>
      </g>
      <polygon points="328,18 370,58 119,309 49,309 288,58" fill="var(--orange)"/>
      <g stroke="#fff" stroke-width="1.2" opacity=".7">
        <line x1="300" y1="88" x2="340" y2="122"/><line x1="258" y1="132" x2="296" y2="166"/>
        <line x1="214" y1="177" x2="252" y2="211"/><line x1="170" y1="222" x2="208" y2="256"/>
        <line x1="128" y1="266" x2="166" y2="300"/>
      </g>
      <g fill="#fff">
        <circle cx="288" cy="97" r="8"/><circle cx="245" cy="142" r="8"/>
        <circle cx="200" cy="187" r="8"/><circle cx="155" cy="232" r="8"/><circle cx="112" cy="280" r="8"/>
      </g>
    </svg>
    <div class="cover-brand"><span class="mark"></span><div class="name">Linden Peak</div><div class="sub">MANAGEMENT</div></div>
    <h1 class="cover-headline"><span class="l1">SUPERIOR RESULTS</span><span class="l2">DEMAND A UNIQUE</span><span class="l3">APPROACH</span></h1>
    <div class="cover-url">lindenpr.kzqt4-rv7.b9servo.com</div>
    <div class="cover-rule"></div>
  </section>
</div>

<!-- grid: cover -->
<section class="slide cover" style="left:45px;top:862px">
  <svg class="art" viewBox="0 0 549 309">
    <defs>
      <linearGradient id="deskB" x1="0" y1="0" x2="1" y2="1">
        <stop offset="0" stop-color="#2f3a4b"/><stop offset=".55" stop-color="#8d939c"/><stop offset="1" stop-color="#d9dbde"/>
      </linearGradient>
    </defs>
    <polygon points="0,0 410,0 138,309 0,309" fill="var(--blue)"/>
    <g role="img" aria-label="Photo of business advisors reviewing documents at a desk">
      <polygon points="0,0 272,0 70,210 0,180" fill="url(#deskB)"/>
    </g>
    <polygon points="328,18 370,58 119,309 49,309 288,58" fill="var(--orange)"/>
    <g stroke="#fff" stroke-width="1.2" opacity=".7">
      <line x1="300" y1="88" x2="340" y2="122"/><line x1="258" y1="132" x2="296" y2="166"/>
      <line x1="214" y1="177" x2="252" y2="211"/><line x1="170" y1="222" x2="208" y2="256"/>
      <line x1="128" y1="266" x2="166" y2="300"/>
    </g>
    <g fill="#fff">
      <circle cx="288" cy="97" r="8"/><circle cx="245" cy="142" r="8"/>
      <circle cx="200" cy="187" r="8"/><circle cx="155" cy="232" r="8"/><circle cx="112" cy="280" r="8"/>
    </g>
  </svg>
  <div class="cover-brand"><span class="mark"></span><div class="name">Linden Peak</div><div class="sub">MANAGEMENT</div></div>
  <h2 class="cover-headline"><span class="l1">SUPERIOR RESULTS</span><span class="l2">DEMAND A UNIQUE</span><span class="l3">APPROACH</span></h2>
  <div class="cover-url">lindenpr.kzqt4-rv7.b9servo.com</div>
  <div class="cover-rule"></div>
</section>

<!-- services -->
<section class="slide services" style="left:615px;top:862px">
  <svg class="art" viewBox="0 0 549 309">
    <g id="svc">
      <polygon points="105,76 149,120 105,164 61,120" fill="var(--orange)"/>
      <polygon points="105,80 145,120 105,160 65,120" fill="#fff"/>
      <polygon points="105,83 142,120 105,157 68,120" fill="var(--blue)"/>
      <line x1="105" y1="166" x2="105" y2="180" stroke="var(--orange)" stroke-dasharray="1.5 2"/>
      <circle cx="105" cy="183" r="2.5" fill="var(--orange)"/>
    </g>
    <use href="#svc" x="172"/><use href="#svc" x="345"/>
    <g fill="none" stroke="#fff" stroke-width="2" stroke-linecap="round">
      <circle cx="105" cy="118" r="10"/><path d="M101 114h6M101 118h6M104 111v14"/>
      <path d="M96 134q9 -5 18 0"/>
      <ellipse cx="277" cy="126" rx="11" ry="3.5"/><ellipse cx="277" cy="119" rx="11" ry="3.5"/>
      <circle cx="272" cy="112" r="7"/>
      <path d="M438 132v-8M444 132v-12M450 132v-16M456 132v-20M436 118l10 -8 6 3 8 -7"/>
      <path d="M433 134h28"/>
    </g>
  </svg>
  <h2 class="slide-title"><span class="accent">LOREM</span> IPSUM TEXT</h2>
  <div class="mini-brand"><div class="name">Linden Peak</div><div class="sub">MANAGEMENT</div></div>
  <p class="copy copy-center service-caption" style="left:45px">Lorem Ipsum is simply dummy text of the printing and typesetting industry. Lorem Ipsum has been the industry's standard.</p>
  <p class="copy copy-center service-caption" style="left:217px">Lorem Ipsum is simply dummy text of the printing and typesetting industry. Lorem Ipsum has been the industry's standard.</p>
  <p class="copy copy-center service-caption" style="left:390px">Lorem Ipsum is simply dummy text of the printing and typesetting industry. Lorem Ipsum has been the industry's standard.</p>
  <div class="slide-footer">lindenpr.kzqt4-rv7.b9servo.com</div>
  <div class="page-no">01</div>
</section>

<!-- bullet points -->
<section class="slide points" style="left:45px;top:1206px">
  <svg class="art" viewBox="0 0 549 309">
    <defs>
      <linearGradient id="phoneDesk" x1="0" y1="0" x2="1" y2="1">
        <stop offset="0" stop-color="#e9e9e9"/><stop offset=".6" stop-color="#cfd2d6"/><stop offset="1" stop-color="#a7adb4"/>
      </linearGradient>
    </defs>
    <polygon points="0,0 125,0 0,240" fill="var(--blue)"/>
    <polygon points="142,25 270,153 142,281 14,153" fill="none" stroke="var(--blue)" stroke-width="2"/>
    <polygon points="170,68 262,160 170,252 78,160" fill="var(--orange)"/>
    <polygon points="135,52 235,152 135,252 35,152" fill="#fff"/>
    <g role="img" aria-label="Photo of a hand holding a smartphone above a desk with a calculator">
      <polygon points="135,60 227,152 135,244 43,152" fill="url(#phoneDesk)"/>
    </g>
  </svg>
  <h3 class="list-heading"><span class="accent">LOREM IPSUM IS</span> SIMPLY DUMMY TEXT</h3>
  <p class="copy copy-strong point" style="top:100px">Lorem Ipsum is simply dummy text of the printing and typesetting industry. Lorem Ipsum has been the industry's standard dummy.</p>
  <p class="copy copy-strong point" style="top:152px">Lorem Ipsum is simply dummy text of the printing and typesetting industry. Lorem Ipsum has been the industry's standard dummy.</p>
  <p class="copy copy-strong point" style="top:204px">Lorem Ipsum is simply dummy text of the printing and typesetting industry. Lorem Ipsum has been the industry's standard dummy.</p>
  <div class="mini-brand"><div class="name">Linden Peak</div><div class="sub">MANAGEMENT</div></div>
  <div class="slide-footer">lindenpr.kzqt4-rv7.b9servo.com</div>
  <div class="page-no">02</div>
</section>

<!-- text with coins -->
<section class="slide text-image" style="left:615px;top:1206px">
  <svg class="art" viewBox="0 0 549 309">
    <defs>
      <linearGradient id="coinsA" x1="0" y1="0" x2="1" y2="1">
        <stop offset="0" stop-color="#f4f4f4"/><stop offset=".5" stop-color="#b9b4a8"/><stop offset="1" stop-color="#3d6fb3"/>
      </linearGradient>
    </defs>
    <polygon points="405,10 545,150 405,290 265,150" fill="none" stroke="var(--blue)" stroke-width="2"/>
    <polygon points="405,80 500,175 405,270 310,175" fill="var(--orange)"/>
    <polygon points="405,44 503,142 405,240 307,142" fill="#fff"/>
    <g role="img" aria-label="Photo of stacked coins beside blue pens on paperwork">
      <polygon points="405,52 495,142 405,232 315,142" fill="url(#coinsA)"/>
    </g>
  </svg>
  <h2 class="slide-title"><span class="accent">LOREM IPSUM</span> IS A SIMPLY TEXT</h2>
  <div class="mini-brand"><div class="name">Linden Peak</div><div class="sub">MANAGEMENT</div></div>
  <div class="copy" style="position:absolute;left:16px;top:62px;width:236px">
    <p>Lorem Ipsum is simply dummy text of the printing and typesetting industry. Lorem Ipsum has been the industry's standard dummy text ever since the 1500s, when an unknown printer took a galley of type and scrambled it to make a type specimen book. It has survived not only five centuries, but also the leap into electronic typesetting, remaining essentially unchanged. It was popularised in the 1960s with the release of Letraset sheets containing Lorem Ipsum passages, and more recently with desktop publishing software like Aldus PageMaker including versions of Lorem Ipsum.</p>
    <p style="margin-top:8px">Lorem Ipsum is simply dummy text of the printing and typesetting industry. Lorem Ipsum has been the industry's standard dummy text ever since the 1500s, when an unknown printer took a galley of type and scrambled it to make a type specimen book.</p>
  </div>
  <div class="slide-footer">lindenpr.kzqt4-rv7.b9servo.com</div>
  <div class="page-no">03</div>
</section>

<!-- blue band with coins -->
<section class="slide band-image" style="left:45px;top:1550px">
  <svg class="art" viewBox="0 0 549 309">
    <defs>
      <linearGradient id="coinsB" x1="0" y1="0" x2="1" y2="1">
        <stop offset="0" stop-color="#5a5f55"/><stop offset=".5" stop-color="#c9c5b8"/><stop offset="1" stop-color="#b0553f"/>
      </linearGradient>
    </defs>
    <polygon points="0,70 330,70 262,240 0,240" fill="var(--blue)"/>
    <polygon points="427,15 540,150 427,285 314,150" fill="none" stroke="var(--blue)" stroke-width="2"/>
    <polygon points="427,110 500,183 427,256 354,183" fill="var(--orange)"/>
    <polygon points="427,46 523,142 427,238 331,142" fill="#fff"/>
    <g role="img" aria-label="Photo of a stack of coins on banknotes">
      <polygon points="427,54 515,142 427,230 339,142" fill="url(#coinsB)"/>
    </g>
  </svg>
  <h2 class="slide-title"><span class="accent">LOREM IPSUM</span> IS A SIMPLY TEXT</h2>
  <div class="mini-brand"><div class="name">Linden Peak</div><div class="sub">MANAGEMENT</div></div>
  <div class="copy band-copy">
    <p>Lorem Ipsum is simply dummy text of the printing and typesetting industry. Lorem Ipsum has been the industry's standard dummy text ever since the 1500s, when an unknown printer took a galley of type and scrambled it to make a type specimen book. It has survived not only five centuries, but also the leap into electronic typesetting, remaining essentially unchanged. It was popularised in the 1960s with the release of Letraset sheets containing Lorem Ipsum passages, and more recently with desktop publishing software like Aldus PageMaker including versions of Lorem Ipsum.</p>
    <p>Lorem Ipsum is simply dummy text of the printing and typesetting industry. Lorem Ipsum has been the industry's standard dummy text ever since the 1500s, when an unknown printer took a galley of type and scrambled it to make a type specimen book.</p>
  </div>
  <div class="slide-footer">lindenpr.kzqt4-rv7.b9servo.com</div>
  <div class="page-no">04</div>
</section>

<!-- five tabs -->
<section class="slide tabs" style="left:615px;top:1550px">
  <svg class="art" viewBox="0 0 549 309">
    <polygon points="22,45 112,45 112,170 67,215 22,170" fill="#c2c2c2"/>
    <polygon points="127,45 217,45 217,170 172,215 127,170" fill="#a6a6a6"/>
    <polygon points="232,45 322,45 322,170 277,215 232,170" fill="#8a8a8a"/>
    <polygon points="337,45 427,45 427,170 382,215 337,170" fill="#666"/>
    <polygon points="442,45 532,45 532,170 487,215 442,170" fill="#363636"/>
    <g stroke="#fff" stroke-width=".6" opacity=".6">
      <path d="M30 77h74M30 99h74M30 121h74M135 77h74M135 99h74M135 121h74M240 77h74M240 99h74M240 121h74M345 77h74M345 99h74M345 121h74M450 77h74M450 99h74M450 121h74"/>
    </g>
    <g fill="none" stroke="#fff" stroke-width="2" stroke-linejoin="round">
      <polygon points="67,155 92,180 67,205 42,180"/><polygon points="172,155 197,180 172,205 147,180"/>
      <polygon points="277,155 302,180 277,205 252,180"/><polygon points="382,155 407,180 382,205 357,180"/>
      <polygon points="487,155 512,180 487,205 462,180"/>
    </g>
    <g fill="none" stroke="#fff" stroke-width="1.4" stroke-linecap="round">
      <circle cx="67" cy="178" r="5"/><path d="M60 188q7 -4 14 0"/>
      <circle cx="170" cy="180" r="6"/><path d="M176 176h4M176 180h4M176 184h4"/>
      <path d="M271 185l6 -8 6 8M277 177v9"/>
      <circle cx="378" cy="175" r="2.5"/><circle cx="386" cy="175" r="2.5"/><path d="M374 186q4 -6 8 0q4 -6 8 0"/>
      <path d="M480 186h14M483 186v-6h8v6M487 177v-3"/>
    </g>
  </svg>
  <h2 class="slide-title"><span class="accent">LOREM IPSUM</span> IS A SIMPLY TEXT</h2>
  <div class="mini-brand"><div class="name">Linden Peak</div><div class="sub">MANAGEMENT</div></div>
  <div class="tab-text" style="left:22px">Lorem Ipsum is simply<br>Lorem Ipsum is simply<br>Lorem Ipsum is simply<br>Lorem Ipsum is simply</div>
  <div class="tab-text" style="left:127px">Lorem Ipsum is simply<br>Lorem Ipsum is simply<br>Lorem Ipsum is simply<br>Lorem Ipsum is simply</div>
  <div class="tab-text" style="left:232px">Lorem Ipsum is simply<br>Lorem Ipsum is simply<br>Lorem Ipsum is simply<br>Lorem Ipsum is simply</div>
  <div class="tab-text" style="left:337px">Lorem Ipsum is simply<br>Lorem Ipsum is simply<br>Lorem Ipsum is simply<br>Lorem Ipsum is simply</div>
  <div class="tab-text" style="left:442px">Lorem Ipsum is simply<br>Lorem Ipsum is simply<br>Lorem Ipsum is simply<br>Lorem Ipsum is simply</div>
  <p class="copy copy-center" style="position:absolute;left:30px;top:238px;width:490px;font-size:5.5px">Lorem Ipsum is simply dummy text of the printing and typesetting industry. Lorem Ipsum has been the industry's standard dummy text ever since the 1500s, when an unknown printer took a galley of type and scrambled it to make a type specimen book. It has survived not only five centuries.</p>
  <div class="slide-footer">lindenpr.kzqt4-rv7.b9servo.com</div>
  <div class="page-no">05</div>
</section>

<!-- two profiles -->
<section class="slide profiles" style="left:45px;top:1894px">
  <svg class="art" viewBox="0 0 549 309">
    <g id="prof">
      <polygon points="67,22 110,65 67,108 24,65" fill="var(--orange)"/>
      <polygon points="67,26 106,65 67,104 28,65" fill="#fff"/>
      <polygon points="67,29 103,65 67,101 31,65" fill="var(--blue)"/>
      <circle cx="67" cy="58" r="7" fill="#fff"/>
      <path d="M53 80q14 -16 28 0z" fill="#fff"/>
    </g>
    <use href="#prof" x="296"/>
    <line x1="277" y1="57" x2="277" y2="267" stroke="var(--orange)" stroke-dasharray="1.5 2.5"/>
  </svg>
  <h2 class="slide-title"><span class="accent">LOREM IPSUM</span> IS A SIMPLY TEXT</h2>
  <div class="mini-brand"><div class="name">Linden Peak</div><div class="sub">MANAGEMENT</div></div>
  <div class="copy profile-copy" style="left:132px;top:68px"><div class="label">LOREM IPSUM</div>Lorem Ipsum is simply dummy text of the printing and typesetting industry. Lorem Ipsum has been the industry's standard.</div>
  <div class="copy profile-copy" style="left:428px;top:68px"><div class="label">LOREM IPSUM</div>Lorem Ipsum is simply dummy text of the printing and typesetting industry. Lorem Ipsum has been the industry's standard.</div>
  <div class="copy" style="position:absolute;left:18px;top:182px;width:240px"><div class="col-heading">LOREM IPSUM IS SIMPLY DUMMY TEXT OF THE PRINTING</div>Lorem Ipsum is simply dummy text of the printing and typesetting industry. Lorem Ipsum has been the industry's standard dummy text ever since the 1500s, when an unknown printer took a galley of type and scrambled it to make a type specimen book. It has survived not only five centuries.</div>
  <div class="copy" style="position:absolute;left:316px;top:182px;width:222px"><div class="col-heading">LOREM IPSUM IS SIMPLY DUMMY TEXT OF THE PRINTING</div>Lorem Ipsum is simply dummy text of the printing and typesetting industry. Lorem Ipsum has been the industry's standard dummy text ever since the 1500s, when an unknown printer took a galley of type and scrambled it to make a type specimen book. It has survived not only five centuries.</div>
  <div class="slide-footer">lindenpr.kzqt4-rv7.b9servo.com</div>
  <div class="page-no">06</div>
</section>

<!-- contact -->
<section class="slide contact" style="left:615px;top:1894px">
  <div class="contact-brand"><div class="name">Linden Peak</div><div class="sub">MANAGEMENT</div></div>
  <div class="contact-band">
    <h3>LOREM IPSUM</h3>
    <p>Lorem Ipsum is simply dummy text of the printing and typesetting industry. Lorem Ipsum has been the industry's standard dummy text ever since the 1500s, when an unknown printer took a galley of type and scrambled it to make a type specimen book. It has survived not only five centuries, but also the leap into electronic typesetting, remaining essentially unchanged. It was popularised in the 1960s with the release of Letraset sheets containing Lorem Ipsum passages, and more recently with desktop publishing software like Aldus.</p>
  </div>
  <div class="call-line">CALL US TODAY<span class="phone">800-555-0143</span></div>
  <div class="info-line" style="top:222px"><span class="dot"></span>Lorem Ipsum is simply text 41207815</div>
  <div class="info-line" style="top:234px"><span class="dot"></span>info@lindenpeak.com</div>
</section>

</body>
</html>
```